Booth flyer

I am looking for a flyer to pass out either at a booth that is set up at an event or to place as a flyer on a car. Quikko Tza is an affordable light reaction training device that will fit everyone's budget and flexible enough for any imaginable use. Our website is Quikkotza.online and Instagram is Quikko.Tza

```html
<!DOCTYPE html>
<html lang="en">
<head>
<meta charset="utf-8">
<title>Quikko Tza – Reaction Light Training</title>
<link href="https://fonts.googleapis.com/css2?family=Rajdhani:wght@300;400;500;600;700&display=swap" rel="stylesheet">
<style>
  :root{
    --red:#e63743;
    --pink:#f9c6cc;
    --charcoal:#333336;
    --ink:#2b2b2e;
    --muted:#6a6a6e;
    --white:#ffffff;
    --kit-blue:#3560b8;
    --grass:#5a9634;
    --grass-dark:#3e7722;
  }
  *{margin:0;padding:0;box-sizing:border-box}
  html,body{width:846px;height:1200px;overflow:hidden;background:var(--white)}
  body{font-family:"Rajdhani",sans-serif;color:var(--ink);position:relative}

  .brand{position:absolute;left:48px;top:40px;display:flex;align-items:center;gap:12px}
  .brand-dot{width:22px;height:22px;border-radius:50%;background:var(--red)}
  .brand-name{font-size:46px;font-weight:700;color:var(--ink);letter-spacing:0.5px;line-height:1}

  .masthead{position:absolute;right:47px;top:36px;text-align:right;line-height:1}
  .masthead-title{font-size:29px;font-weight:600;letter-spacing:0.8px;color:var(--ink)}
  .masthead-url{font-size:26px;font-weight:300;letter-spacing:0.5px;color:var(--ink);margin-top:1px}
  .masthead-social{font-size:15px;font-weight:500;letter-spacing:0.8px;color:var(--muted);margin-top:6px}

  .promo{position:absolute;left:0;top:131px;width:423px;height:470px;background:var(--red);color:var(--white)}
  .headline{position:absolute;left:49px;top:78px;font-size:62px;font-weight:700;line-height:45px;letter-spacing:0.3px}
  .tagline{position:absolute;left:49px;top:283px;font-size:27px;font-weight:700;line-height:25px;color:var(--pink);letter-spacing:0.3px}
  .flex-note{position:absolute;left:49px;top:352px;font-size:21.5px;font-weight:600;line-height:21px;letter-spacing:0.3px}

  .info{position:absolute;left:0;top:601px;width:423px;height:469px;background:var(--charcoal);color:var(--white)}
  .info h2{position:absolute;left:47px;font-size:25.5px;font-weight:700;line-height:24px;letter-spacing:0.3px}
  .info .game{top:78px}
  .info .benefits-title{top:298px}
  .body-copy{position:absolute;left:47px;top:135px;width:350px;font-size:18px;font-weight:400;line-height:22px}
  .body-copy strong{font-weight:700}
  .benefits{position:absolute;left:48px;top:336px;display:flex}
  .benefit{border-left:3px solid var(--white);padding-left:6px;font-size:18px;font-weight:700;line-height:15.7px;color:#bdbdc2;letter-spacing:0.2px}
  .benefit:nth-child(1){width:139px}
  .benefit:nth-child(2){width:101px}

  .photo{position:absolute;left:423px;top:131px;width:423px;height:939px;
    background:linear-gradient(180deg,var(--kit-blue) 0%,#4a7bb0 25%,#6d9a6a 50%,var(--grass) 70%,var(--grass-dark) 100%)}

  .contact{position:absolute;top:1126px;left:0;width:846px;height:30px;font-size:19px;font-weight:400;color:var(--ink)}
  .contact-item{position:absolute;top:0;display:flex;align-items:center;gap:10px;line-height:1}
  .contact-item svg{width:22px;height:25px}
  .divider{position:absolute;top:7px;width:1px;height:13px;background:#c9c9c9}
</style>
</head>
<body>
  <header>
    <div class="brand"><span class="brand-dot"></span><span class="brand-name">Quikko Tza</span></div>
    <div class="masthead">
      <div class="masthead-title">REACTION LIGHT TRAINING</div>
      <div class="masthead-url">WWW.QUIKKOTZA.ONLINE</div>
      <div class="masthead-social">INSTAGRAM @QUIKKO.TZA</div>
    </div>
  </header>

  <section class="promo">
    <h1 class="headline">BRING YOUR<br>TRAINING<br>TO THE NEXT<br>LEVEL</h1>
    <p class="tagline">AFFORDABLE LIGHT REACTION<br>TRAINING DEVICE</p>
    <p class="flex-note">FLEXIBLE ENOUGH FOR ANY<br>IMAGINABLE USE</p>
  </section>

  <section class="info">
    <h2 class="game">UP YOUR GAME WITH<br>REACTION TRAINING LIGHTS</h2>
    <p class="body-copy">An easy to use, multi-light training system <strong>perfect for improving your visual processing</strong> in combination with the appropriate athletic response. Our training lights are portable and can be arranged in any configuration.</p>
    <h2 class="benefits-title">KEY BENEFITS</h2>
    <div class="benefits">
      <div class="benefit">IMPROVED<br>OVERALL<br>PERFORMANCE</div>
      <div class="benefit">IMPROVED<br>DECISION<br>MAKING</div>
      <div class="benefit">IMPROVED<br>VISUAL<br>RESPONSE</div>
    </div>
  </section>

  <div class="photo" role="img" aria-label="Photo of a soccer player in blue and white kit on green grass, with three reaction lights on tripods and a black carry case in front"></div>

  <footer class="contact">
    <div class="contact-item" style="left:48px">
      <svg viewBox="0 0 22 25"><polygon points="11,0 22,6 22,19 11,25 0,19 0,6" fill="var(--red)"/><path d="M11 6.5a4 4 0 0 0-4 4c0 3 4 7 4 7s4-4 4-7a4 4 0 0 0-4-4z" fill="none" stroke="#fff" stroke-width="1.4"/><circle cx="11" cy="10.5" r="1.4" fill="#fff"/></svg>
      <span>Oakridge, California</span>
    </div>
    <div class="divider" style="left:294px"></div>
    <div class="contact-item" style="left:350px">
      <svg viewBox="0 0 22 25"><polygon points="11,0 22,6 22,19 11,25 0,19 0,6" fill="var(--red)"/><path d="M7.5 7.5l2 0 1 3-1.3 1a6 6 0 0 0 3 3l1-1.3 3 1v2a1 1 0 0 1-1 1A9 9 0 0 1 6.5 8.5a1 1 0 0 1 1-1z" fill="none" stroke="#fff" stroke-width="1.2"/></svg>
      <span>Tel: (925) 555-0148</span>
    </div>
    <div class="divider" style="left:569px"></div>
    <div class="contact-item" style="left:623px">
      <svg viewBox="0 0 22 25"><polygon points="11,0 22,6 22,19 11,25 0,19 0,6" fill="var(--red)"/><rect x="5.5" y="8.5" width="11" height="8" fill="none" stroke="#fff" stroke-width="1.3"/><path d="M5.5 8.5l5.5 4.5 5.5-4.5" fill="none" stroke="#fff" stroke-width="1.3"/></svg>
      <span>mail@quikkotza.com</span>
    </div>
  </footer>
</body>
</html>
```